Notary Signing Agent Need Business card Design

Need a Business card design for my new company. RT Velo-Brisk LLC
Mobile Notary Signing Agent. I go to the customer for closing of Mortgage's Documents . possible signs of honesty, integrity and confidentiality.

Work with Title company to Notary Mortgage closing.

My Target Market is Title companies. Banks and Financial Institution.

Color Blue to Black Professional ) if needed some Green Little Red

And possible a company logo.

Mobile ( travel to clients ) Integrity, Honest Trustworthy. A show of Professional services.

Would like company name and my name on card

Use both sides and front with business name and my name. phone numbers.

Target Market(s)

Title company, Banks mortgage company

Industry/Entity Type

Travel

Contact Information for Business Card

Notary, Certified signing agent, Mobile

Colors
0455a3

Requirements
Must have
• Name of company , owners name phone number,
Nice to have
• blue and black color like a professional look but not limit to these only.
• a stand out from other cards .

```html
<!DOCTYPE html>
<html lang="en">
<head>
<meta charset="utf-8">
<title>RT Velo-Brisk LLC – Business Card</title>
<link rel="stylesheet" href="https://fonts.googleapis.com/css2?family=Cousine&family=Open+Sans:wght@400;700&display=swap">
<style>
  :root {
    --page-bg: #e9eaed;
    --card-blue: #2d58a6;
    --card-white: #ffffff;
    --icon-dark: #111318;
    --label-grey: #9a9ca3;
  }
  * { margin: 0; padding: 0; box-sizing: border-box; }
  html, body { width: 1200px; height: 675px; overflow: hidden; }
  body {
    background: var(--page-bg);
    position: relative;
    font-family: "Open Sans", Arial, sans-serif;
  }
  .card {
    position: absolute;
    width: 525px;
    height: 300px;
    background: var(--card-blue);
    color: var(--card-white);
    overflow: hidden;
    box-shadow: 0 6px 18px rgba(0,0,0,.18);
  }
  .card--back { left: 50px; top: 188px; }
  .card--front { left: 625px; top: 188px; }
  .card__shapes { position: absolute; inset: 0; }
  .side-label {
    position: absolute;
    font-family: "Cousine", monospace;
    font-size: 20px;
    letter-spacing: 2px;
    color: var(--label-grey);
  }
  .side-label--back { left: 50px; top: 500px; }
  .side-label--front { left: 625px; top: 500px; }

  .company {
    position: absolute;
    font-family: "Cousine", monospace;
    white-space: nowrap;
  }
  .mark {
    position: absolute;
    width: 34px; height: 34px;
    border-radius: 50%;
    background: var(--card-white);
  }
  .holder { position: absolute; white-space: nowrap; }
  .holder__name {
    font-size: 21px;
    font-weight: 400;
    line-height: 1;
    letter-spacing: .3px;
  }
  .holder__name strong { font-weight: 700; }
  .holder__role {
    font-size: 9px;
    letter-spacing: .4px;
    margin-top: 3px;
  }
  .contacts { position: absolute; list-style: none; }
  .contacts li {
    display: flex;
    align-items: center;
    gap: 10px;
    font-size: 10px;
    letter-spacing: .4px;
    height: 22px;
  }
  .contacts svg { width: 17px; height: 17px; flex: none; }

  /* back */
  .card--back .mark { left: 48px; top: 78px; }
  .card--back .company { left: 130px; top: 68px; font-size: 15px; letter-spacing: 1px; }
  .card--back .holder { left: 22px; top: 200px; }
  .card--back .contacts { left: 355px; top: 124px; }

  /* front */
  .card--front .mark { left: 245px; top: 98px; }
  .card--front .company { left: 0; right: 0; text-align: center; top: 146px; font-size: 17px; letter-spacing: 3px; }
  .card--front .holder { left: 40px; top: 180px; }
  .card--front .contacts { left: 375px; top: 222px; }
</style>
</head>
<body>

<section class="card card--back" aria-label="Business card back side">
  <svg class="card__shapes" viewBox="0 0 525 300" aria-hidden="true">
    <polygon points="445,0 525,0 525,185 505,185" fill="var(--card-white)"/>
    <polygon points="12,300 50,262 315,262 285,300" fill="var(--card-white)"/>
    <g stroke="var(--card-white)" stroke-width="1.2">
      <line x1="128" y1="40" x2="448" y2="40"/>
      <line x1="128" y1="50" x2="452" y2="50"/>
      <line x1="128" y1="60" x2="456" y2="60"/>
    </g>
  </svg>
  <span class="mark" aria-hidden="true"></span>
  <p class="company">RT Velo-Brisk LLC</p>
  <ul class="contacts">
    <li>
      <svg viewBox="0 0 17 17" aria-hidden="true"><rect width="17" height="17" rx="3" fill="var(--icon-dark)"/><rect x="4" y="7" width="9" height="6" rx="1" fill="var(--card-white)"/><rect x="6" y="4" width="5" height="3" fill="var(--card-white)"/></svg>
      <span>555-201-4837</span>
    </li>
    <li>
      <svg viewBox="0 0 17 17" aria-hidden="true"><rect width="17" height="17" rx="3" fill="var(--icon-dark)"/><rect x="5.5" y="3" width="6" height="11" rx="1" fill="none" stroke="var(--card-white)" stroke-width="1.4"/></svg>
      <span>555-318-6620</span>
    </li>
  </ul>
  <div class="holder">
    <p class="holder__name">DANIEL R <strong>HOLT</strong></p>
    <p class="holder__role">NOTARY SIGNING AGENT</p>
  </div>
</section>

<section class="card card--front" aria-label="Business card front side">
  <svg class="card__shapes" viewBox="0 0 525 300" aria-hidden="true">
    <polygon points="140,0 395,0 360,35 170,35" fill="var(--card-white)"/>
    <polygon points="110,300 150,255 345,255 390,300" fill="var(--card-white)"/>
    <g stroke="var(--card-white)" stroke-width="1.2">
      <line x1="0" y1="76" x2="225" y2="76"/>
      <line x1="0" y1="86" x2="225" y2="86"/>
      <line x1="0" y1="96" x2="225" y2="96"/>
      <line x1="300" y1="130" x2="525" y2="130"/>
      <line x1="300" y1="140" x2="525" y2="140"/>
      <line x1="300" y1="150" x2="525" y2="150"/>
    </g>
  </svg>
  <span class="mark" aria-hidden="true"></span>
  <p class="company">RT VELO - BRISK LLC</p>
  <div class="holder">
    <p class="holder__name">DANIEL R <strong>HOLT</strong></p>
    <p class="holder__role">NOTARY SIGNING AGENT</p>
  </div>
  <ul class="contacts">
    <li>
      <svg viewBox="0 0 17 17" aria-hidden="true"><rect width="17" height="17" rx="3" fill="var(--icon-dark)"/><rect x="4" y="7" width="9" height="6" rx="1" fill="var(--card-white)"/><rect x="6" y="4" width="5" height="3" fill="var(--card-white)"/></svg>
      <span>555-201-4837</span>
    </li>
    <li>
      <svg viewBox="0 0 17 17" aria-hidden="true"><rect width="17" height="17" rx="3" fill="var(--icon-dark)"/><rect x="5.5" y="3" width="6" height="11" rx="1" fill="none" stroke="var(--card-white)" stroke-width="1.4"/></svg>
      <span>555-318-6620</span>
    </li>
  </ul>
</section>

<p class="side-label side-label--back">BACK SIDE</p>
<p class="side-label side-label--front">FRONT SIDE</p>

</body>
</html>
```